HollowPine Ventures Inc. Business Card Design

My business is custom renovations and homes.I would need to have a new business logo created to go along with my company name. The business card should be of a modern style as this is the market I am focused on. I would need my contact information and website posted on the card. I would also like to list a few of the tasks I conduct on the card (such as: Renovations, Additions, Repairs, New Homes, Design, Consultations). On the reverse of the card I currently have just my logo and my motto, "Shaping A Bold Path". However, I am open to completely changing everything as I am starting a new year and would like to excel further. Any new ideas and suggestions are always welcomed. Thank you.

Target Market(s)

Upscale residential and commercial renovations and builds

Industry/Entity Type

Business

Contact Information for Business Card

I would like the design to be able to be laser cut or burnt onto a wooden business card. I will be creating one option of cards for really loyal customers (wooden) and a second option for the everyday customer (paper).

Font styles to use
Other font styles liked:
• Calibri / anything of mordern taste

Colors
f37122
5c5c5c
474747
ffffff

Requirements
Must have
• I would like the colours of my business to be a sharp orange and grey. I believe this will symbolize a modern style. I am open to other suggestions if this is not suitable for the designers tastes. My contact info as follows:
• Will Marsh
• President
• HollowPine Ventures Inc.
• 555-214-3987
• will@hollowpineventures.example
• I would like my website (currently under construction) hollowpineventures.example on the card aswell.
Nice to have
• Along with a modern logo representing HollowPine, I would like something on the card besides the logo and contact information. Perhaps a small background design. I feel it may be nice to have my services listed on the card (in smaller font on the bottom) Renovations, Additions, Repairs, Design, Consultations.
Should not have
• The business card should not have too many different colors. Should not have rounded corners.

```html
<!DOCTYPE html>
<html lang="en">
<head>
<meta charset="utf-8">
<title>HollowPine Ventures Inc. — Business Card</title>
<link href="https://fonts.googleapis.com/css2?family=Open+Sans:wght@600;700&display=swap" rel="stylesheet">
<style>
  :root {
    --orange: #f37122;
    --wood: #5c5c5c;
    --plank-line: #474747;
    --ink: #3a3a3a;
    --highlight: rgba(255,255,255,0.35);
    --page: #ffffff;
  }
  html, body {
    margin: 0;
    width: 1200px;
    height: 1200px;
    overflow: hidden;
    background: var(--page);
    font-family: "Open Sans", Calibri, sans-serif;
  }
  .card {
    position: absolute;
    left: 120px;
    top: 220px;
    width: 950px;
    height: 736px;
    background: linear-gradient(180deg, #626262 0%, var(--wood) 50%, #585858 100%);
    overflow: hidden;
  }
  .plank-line {
    position: absolute;
    left: 0;
    width: 100%;
    height: 3px;
    background: var(--plank-line);
    box-shadow: 0 1px 0 rgba(255,255,255,0.08);
  }
  .embossed {
    position: absolute;
    margin: 0;
    color: var(--ink);
    font-weight: 700;
    white-space: nowrap;
    text-shadow: 1px 1px 0 var(--highlight), -1px -1px 0 rgba(0,0,0,0.25);
  }
  .contact-name { left: 40px; top: 72px; font-size: 54px; font-weight: 600; }
  .contact-title { left: 36px; top: 166px; font-size: 44px; }
  .contact-phone { left: 36px; top: 234px; font-size: 46px; }
  .contact-email { left: 36px; top: 316px; font-size: 31px; }
  .website-tag {
    position: absolute;
    left: 470px;
    top: 38px;
    width: 448px;
    height: 62px;
    background: var(--orange);
    display: flex;
    align-items: center;
    justify-content: center;
  }
  .website-tag .embossed { position: static; font-size: 30px; }
  .brand-name {
    position: absolute;
    left: 446px;
    top: 342px;
    width: 200px;
    text-align: center;
    margin: 0;
    color: var(--orange);
    font-size: 46px;
    font-weight: 700;
  }
  .service-arc { position: absolute; left: 0; top: 0; }
  .service {
    position: absolute;
    background: var(--orange);
    display: flex;
    align-items: center;
    justify-content: center;
  }
  .service .embossed { position: static; font-size: 31px; }
  .service--renovations { left: 44px; top: 504px; width: 226px; height: 94px; }
  .service--additions { left: 278px; top: 504px; width: 176px; height: 94px; }
  .service--repairs { left: 462px; top: 504px; width: 160px; height: 94px; }
  .service--new-homes { left: 629px; top: 504px; width: 217px; height: 98px; }
  .service--consultations { left: 226px; top: 618px; width: 436px; height: 100px; }
  .service--consultations .embossed { font-size: 36px; }
</style>
</head>
<body>
  <div class="card">
    <div class="plank-line" style="top:124px"></div>
    <div class="plank-line" style="top:242px"></div>
    <div class="plank-line" style="top:368px"></div>
    <div class="plank-line" style="top:490px"></div>
    <div class="plank-line" style="top:612px"></div>

    <p class="embossed contact-name">Will Marsh</p>
    <p class="embossed contact-title">President</p>
    <p class="embossed contact-phone">(555) 214-3987</p>
    <p class="embossed contact-email">will@hollowpineventures.example</p>

    <div class="website-tag"><span class="embossed">hollowpineventures.example</span></div>

    <p class="brand-name">HollowPine</p>

    <svg class="service-arc" width="950" height="736" viewBox="0 0 950 736" aria-hidden="true">
      <path d="M152 510 Q 200 452 470 452 Q 740 452 808 510" fill="none" stroke="var(--orange)" stroke-width="8"/>
      <g fill="var(--orange)">
        <rect x="244" y="596" width="6" height="24"/>
        <rect x="362" y="596" width="6" height="24"/>
        <rect x="542" y="596" width="6" height="24"/>
        <rect x="642" y="600" width="6" height="20"/>
      </g>
    </svg>

    <div class="service service--renovations"><span class="embossed">Renovations</span></div>
    <div class="service service--additions"><span class="embossed">Additions</span></div>
    <div class="service service--repairs"><span class="embossed">Repairs</span></div>
    <div class="service service--new-homes"><span class="embossed">New Homes</span></div>
    <div class="service service--consultations"><span class="embossed">Consultations</span></div>
  </div>
</body>
</html>
```